Dental Practice Billboard Design

We are a newer dental practice in need of a simple but appealing billboard for our growing dental practice to attract new patients. The practice is owned by husband and wife dentists and is family friendly in a small town in Kentucky. We try to be very friendly and caring to our patients. Would prefer a blue background for the billboard and our tooth logo to be prominent. We are partial to the Patua One font used in the image below but please feel free to tweak it as you deem necessary. The shape of the uppercase D and lowercase g are why we like that font, so fonts with a similarly shaped “D” and “g” would work as well. Please include our phone number (606) 847-3962. Please see our website Harlowfamilydentistry.com for more info on the practice if needed. Thank you! Looking forward to seeing your creation.
Updates

The dimensions will be 12ft x 24ft (3.6576m x 7.3152m). Apologies for not including this in the original prompt. Thank you all for your submissions.

Industry/Entity Type

Dental

Font styles to use
Other font styles liked:
• Patua One

Colors
0054AA
0677BA
7BADD7
CADEEF
E8F1F8
0094D4
00A9DD
6FCCEA
C7EBF8
E9F6FB
00AB8E
00BBA5
67D7C9
C6EFE9
E9F9F6
59FF00
82FF00
B8FF75
E3FFCB
F4FFEA

Requirements
Must have
• Phone number, website, Logo, Practice name “Harlow Family Dentistry”
Should not have
• A tagline or slogan

```html
<!DOCTYPE html>
<html lang="en">
<head>
<meta charset="utf-8">
<title>Harlow Family Dentistry Billboard</title>
<link rel="stylesheet" href="https://fonts.googleapis.com/css2?family=Patua+One&family=Zilla+Slab:wght@700&family=Open+Sans:ital,wght@1,700&display=swap">
<style>
  :root {
    --backdrop: #dfe9f2;
    --board: #f6f5ef;
    --navy: #2b5882;
    --navy-deep: #24506f;
    --band-left: #2c5c79;
    --band-mid: #2fa54c;
    --band-right: #4b70b4;
    --green: #2ea84a;
    --green-light: #5cc24a;
    --white: #ffffff;
  }
  * { margin: 0; padding: 0; box-sizing: border-box; }
  html, body {
    width: 1200px; height: 799px; overflow: hidden;
    background: var(--backdrop);
  }
  .billboard {
    position: absolute; left: 40px; top: 120px;
    width: 1120px; height: 560px;
    background: var(--board);
    overflow: hidden;
    box-shadow: 0 6px 24px rgba(30, 60, 90, .18);
  }
  .band {
    position: absolute; left: 0; top: 300px;
    width: 100%; height: 92px;
    background: linear-gradient(90deg, var(--band-left) 0%, var(--band-left) 28%, var(--band-mid) 52%, var(--band-right) 82%, var(--band-right) 100%);
    display: flex; align-items: center;
    padding-left: 300px;
  }
  .mark-circle {
    position: absolute; left: 60px; top: 90px;
    width: 210px; height: 210px; border-radius: 50%;
    background: var(--green-light);
  }
  .practice-name {
    position: absolute; left: 300px; top: 40px;
    font-family: "Zilla Slab", "Patua One", serif;
    font-weight: 700; color: var(--navy);
    text-transform: uppercase; line-height: 1;
  }
  .practice-name .main { display: block; font-size: 138px; letter-spacing: 4px; }
  .practice-name .sub { display: block; font-size: 50px; letter-spacing: 3px; margin-top: 4px; color: var(--navy-deep); }
  .website {
    font-family: "Patua One", serif;
    font-size: 54px; color: var(--white); letter-spacing: 1px;
    white-space: nowrap;
  }
  .phone {
    position: absolute; left: 300px; top: 400px;
    font-family: "Open Sans", sans-serif;
    font-weight: 700; font-style: italic;
    font-size: 108px; color: var(--green); letter-spacing: 2px;
    line-height: 1.1; white-space: nowrap;
  }
  .signoff {
    position: absolute; left: 52px; top: 478px;
    display: flex; align-items: center; gap: 10px;
  }
  .signoff .dot {
    width: 26px; height: 26px; border-radius: 50%;
    background: var(--green);
  }
  .signoff .name {
    font-family: "Patua One", serif;
    font-size: 22px; color: var(--navy); line-height: 1.1;
    white-space: nowrap;
  }
</style>
</head>
<body>
  <main class="billboard">
    <div class="band">
      <p class="website">Harlowfamilydentistry.com</p>
    </div>
    <div class="mark-circle" aria-hidden="true"></div>
    <h1 class="practice-name">
      <span class="main">Harlow</span>
      <span class="sub">Family Dentistry</span>
    </h1>
    <p class="phone">(606) 847-3962</p>
    <div class="signoff">
      <span class="dot" aria-hidden="true"></span>
      <span class="name">Harlow<br>Family Dentistry</span>
    </div>
  </main>
</body>
</html>
```